Brightway Inc. Business Card Design

Brightway Inc. is in search of a great clean design for our business cards!

Looking to incorporate our full logo and watermark on side one (however, I am open to having the text and watermark separated within the design.)

On side two, I am looking to have contact information (Name, Position, Phone #, Email, Website (www.thebrightway.ca). Can have the logo and/or watermark as part of the design if applicable.

Please add tagline "Where Shine Counts" on either side 1 or 2. This tagline can be in a sans serif, serif or cursive font as long as it compliments overall design. Capitalization can be title or sentence case depending on how it fits within the design.

Get creative!! Looking for a clean, crisp, premium design! Looking for a glossy card finish with spot UV features when printed. Cards will also be printed with rounded corners. Standard dimensions (3.5 x 2).

Target Market(s)

B2B - primary clients are business owners or property management corporations. (residential jobs are few and far between)

Industry/Entity Type

Business

Contact Information for Business Card

- clean, crisp design
- double sided
- spot UV accents and glossy finish upon printing
- standard business card size (3.5 x 2) with rounded corners
- please see project description for requirements per side

Font styles to use
Sans Serif

Requirements
Must have
• - adequate bleeds with print ready files
• - cohesive design elements between side 1 & 2
• - spot UV elements (can be on both sides or just one, use your discretion)
• - colour pallet should match the logo file provided
• - incorporate tagline "where shine counts" (this tagline can be in a serif or sans serif font as long as it is complimentary to the overall design.
Nice to have
• - Premium elements with a clean design
Should not have
• - Please omit cartoon or whimsical like designs, think premium.
• - Colours should not stray from the pallet of the provided logo.

```html
<!DOCTYPE html>
<html lang="en">
<head>
<meta charset="utf-8">
<title>Brightway Inc. Business Card</title>
<link rel="stylesheet" href="https://fonts.googleapis.com/css2?family=Lato:wght@400;700;900&display=swap">
<style>
  :root {
    --navy: #1b2450;
    --teal: #17b3b6;
    --white: #ffffff;
    --paper: #f4f5f7;
    --ink: #1b2450;
    --muted: #6b6f82;
    --backdrop: #807c84;
  }
  * { box-sizing: border-box; margin: 0; padding: 0; }
  html, body { width: 1200px; height: 675px; overflow: hidden; }
  body {
    background: var(--backdrop);
    font-family: "Lato", sans-serif;
    position: relative;
  }
  .card {
    position: absolute;
    top: 198px;
    width: 490px;
    height: 280px;
    border-radius: 18px;
    overflow: hidden;
    box-shadow: 0 6px 16px rgba(0,0,0,0.25);
  }
  /* Side one */
  .card-front { left: 70px; background: var(--navy); }
  .front-brand {
    position: absolute;
    left: 0; right: 0; top: 108px;
    display: flex; align-items: center; justify-content: center; gap: 10px;
  }
  .brand-square { width: 22px; height: 22px; background: var(--teal); }
  .front-brand .brand-name {
    font-weight: 900; font-size: 38px; letter-spacing: 1px; color: var(--white);
  }
  .tagline {
    position: absolute; left: 0; right: 0; top: 200px;
    text-align: center; color: var(--white); font-size: 17px; letter-spacing: 0.5px;
  }
  /* Side two */
  .card-back { left: 640px; background: var(--paper); }
  .back-band { position: absolute; inset: 0; }
  .holder {
    position: absolute; right: 26px; top: 16px; text-align: right; color: var(--white);
  }
  .holder-name { font-size: 19px; font-weight: 400; }
  .holder-role { font-size: 10px; margin-top: 1px; }
  .back-brand {
    position: absolute; left: 30px; top: 136px;
    display: flex; align-items: center; gap: 7px;
  }
  .back-brand .brand-square { width: 15px; height: 15px; }
  .back-brand .brand-name {
    font-weight: 900; font-size: 23px; color: var(--ink); letter-spacing: 0.5px;
  }
  .divider {
    position: absolute; left: 262px; top: 122px; width: 1px; height: 70px; background: #b9bcc6;
  }
  .contacts {
    position: absolute; left: 282px; top: 120px; list-style: none;
    font-size: 10.5px; color: var(--ink);
  }
  .contacts li { display: flex; align-items: center; gap: 7px; height: 17px; }
  .contacts svg { width: 10px; height: 10px; fill: var(--ink); flex: none; }
  .address {
    position: absolute; left: 64px; top: 202px;
    font-size: 11px; line-height: 15px; color: var(--ink);
  }
</style>
</head>
<body>
  <section class="card card-front" aria-label="Business card, side one">
    <div class="front-brand">
      <span class="brand-square"></span>
      <span class="brand-name">BRIGHTWAY INC.</span>
    </div>
    <p class="tagline">Where Shine Counts</p>
  </section>

  <section class="card card-back" aria-label="Business card, side two">
    <svg class="back-band" viewBox="0 0 490 280" preserveAspectRatio="none" aria-hidden="true">
      <path d="M0 0 H490 V40 C360 50 180 70 0 112 Z" fill="var(--navy)"/>
      <path d="M0 112 C180 70 360 50 490 40 L490 48 C360 56 180 76 0 118 Z" fill="var(--teal)"/>
    </svg>
    <div class="holder">
      <p class="holder-name">Daniel Reyes</p>
      <p class="holder-role">Graphic Designer</p>
    </div>
    <div class="back-brand">
      <span class="brand-square"></span>
      <span class="brand-name">BRIGHTWAY INC.</span>
    </div>
    <div class="divider"></div>
    <ul class="contacts">
      <li><svg viewBox="0 0 10 10"><rect x="2.5" y="0" width="5" height="10" rx="1"/><rect x="3.5" y="1.2" width="3" height="6.5" fill="#f4f5f7"/></svg>0812-5550-1947</li>
      <li><svg viewBox="0 0 10 10"><path d="M2 0.5 L4 2.8 L3 4 C3.6 5.4 4.6 6.4 6 7 L7.2 6 L9.5 8 L8.3 9.5 C4.5 9.3 0.7 5.5 0.5 1.7 Z"/></svg>0812-5550-2083</li>
      <li><svg viewBox="0 0 10 10"><rect x="0" y="2" width="10" height="6.5"/><path d="M0.5 2.5 L5 6 L9.5 2.5" stroke="#f4f5f7" fill="none"/></svg>d.reyes@brightmail.com</li>
      <li><svg viewBox="0 0 10 10"><circle cx="5" cy="5" r="4.5"/><path d="M0.5 5 H9.5 M5 0.5 C2.5 3 2.5 7 5 9.5 M5 0.5 C7.5 3 7.5 7 5 9.5" stroke="#f4f5f7" stroke-width="0.7" fill="none"/></svg>www.thebrightway.ca</li>
    </ul>
    <p class="address">Jl. Melati No. 12<br>Karangsari-Malang 65112<br>Jawa Barat</p>
  </section>
</body>
</html>
```